Business Card for a mobile physiotherapy company

I need a layout for a business card for a mobile physiotherapy company.
Slogan is "Mobile Physiotherapy - Your Road To Recovery"
Phone number is 867-402-5913
Email VantrePhysio@mailbright.ca (subject to change with website)
Website www.VantrePhysio.ca
My name and credentials: Kent Vantre Kent Vantre, BSc(kin), MPT, CAFCI, IMS
Information maybe included: Direct Billing, Services including Physiotherapy, IMS, acupuncture
Maybe include facebook and instagram logos
One side with the logo clean and sharp
Other side with details, try not to look too busy, keep everything concise

```html
<!DOCTYPE html>
<html lang="en">
<head>
<meta charset="UTF-8">
<title>Vantre Therapy – Business Card</title>
<link href="https://fonts.googleapis.com/css2?family=Libre+Baskerville:wght@400;700&family=Open+Sans:wght@400;600;700&display=swap" rel="stylesheet">
<style>
  :root {
    --navy: #2c4a73;
    --green: #1f5a48;
    --ink: #1d1d1d;
    --paper: #ffffff;
    --stage: #e9eaec;
    --serif: "Libre Baskerville", Georgia, serif;
    --sans: "Open Sans", Arial, sans-serif;
  }
  * { margin: 0; padding: 0; box-sizing: border-box; }
  html, body { width: 1200px; height: 960px; overflow: hidden; }
  body {
    background: var(--stage);
    display: flex;
    flex-direction: column;
    align-items: center;
    justify-content: center;
    gap: 32px;
    font-family: var(--sans);
  }
  .card {
    width: 760px;
    height: 434px;
    position: relative;
    overflow: hidden;
    box-shadow: 0 6px 18px rgba(0,0,0,0.18);
  }

  /* Brand name placeholder */
  .brand {
    display: flex;
    align-items: center;
    gap: 12px;
    font-family: var(--sans);
    font-weight: 600;
    white-space: nowrap;
  }
  .brand-dot { border-radius: 50%; flex: none; }

  /* Front */
  .card-front {
    background: var(--navy);
    display: flex;
    flex-direction: column;
    align-items: center;
    justify-content: center;
    gap: 40px;
  }
  .card-front .brand { color: var(--paper); font-size: 46px; }
  .card-front .brand-dot { width: 22px; height: 22px; background: var(--paper); }
  .social-row { display: flex; gap: 46px; }
  .social-slot { width: 38px; height: 38px; background: var(--paper); }

  /* Back */
  .card-back { background: var(--paper); }
  .bottom-band {
    position: absolute; left: 0; right: 0; bottom: 0;
    height: 16px; background: var(--navy);
  }
  .card-back .brand {
    position: absolute; right: 44px; top: 96px;
    color: var(--navy); font-size: 32px;
  }
  .card-back .brand-dot { width: 16px; height: 16px; background: var(--navy); }

  .person { position: absolute; left: 44px; top: 150px; }
  .person-name {
    font-family: var(--serif);
    font-weight: 700;
    font-size: 22px;
    color: var(--navy);
    text-transform: uppercase;
  }
  .person-creds { font-size: 11px; color: var(--ink); margin-top: 3px; }
  .contact-list { list-style: none; margin-top: 10px; }
  .contact-list li {
    display: flex; align-items: center; gap: 8px;
    font-size: 15px; color: var(--ink);
    margin-bottom: 5px;
  }
  .contact-list svg { width: 14px; height: 14px; flex: none; }

  .slogan {
    position: absolute; right: 60px; top: 196px;
    font-family: var(--serif);
    font-weight: 700;
    font-size: 15px;
    color: var(--navy);
  }
  .divider {
    position: absolute; left: 292px; right: 36px; top: 222px;
    height: 2px; background: var(--green);
  }
  .services { position: absolute; right: 44px; top: 240px; text-align: right; }
  .services-title { font-weight: 700; font-size: 16px; color: var(--navy); margin-bottom: 4px; }
  .services-list {
    list-style: none;
    display: grid;
    grid-template-columns: auto auto;
    column-gap: 20px; row-gap: 1px;
    justify-content: end;
    text-align: left;
  }
  .services-list li { font-size: 16px; color: var(--green); }
  .services-list li::before { content: "• "; }
</style>
</head>
<body>

  <section class="card card-front" aria-label="Card front">
    <div class="brand"><span class="brand-dot"></span>Vantre Therapy</div>
    <div class="social-row">
      <span class="social-slot" role="img" aria-label="Social network link"></span>
      <span class="social-slot" role="img" aria-label="Social network link"></span>
    </div>
  </section>

  <section class="card card-back" aria-label="Card back">
    <div class="brand"><span class="brand-dot"></span>Vantre Therapy</div>

    <div class="person">
      <h1 class="person-name">Kent Vantre</h1>
      <p class="person-creds">BSc(kin), MPT, CAFCI, IMS</p>
      <ul class="contact-list">
        <li>
          <svg viewBox="0 0 16 16" aria-hidden="true"><circle cx="8" cy="8" r="7" fill="none" stroke="#2c4a73" stroke-width="1.3"/><path d="M5.5 4.5l1.4 1.6-.8 1c.6 1.2 1.5 2.1 2.7 2.7l1-.8 1.6 1.4-.9 1.2C7.9 11.4 4.6 8.1 4.3 5.4z" fill="#2c4a73"/></svg>
          867-402-5913
        </li>
        <li>
          <svg viewBox="0 0 16 16" aria-hidden="true"><circle cx="8" cy="8" r="7" fill="none" stroke="#2c4a73" stroke-width="1.3"/><rect x="4.3" y="5.3" width="7.4" height="5.4" fill="none" stroke="#2c4a73" stroke-width="1.1"/><path d="M4.3 5.5L8 8.4l3.7-2.9" fill="none" stroke="#2c4a73" stroke-width="1.1"/></svg>
          VantrePhysio@mailbright.ca
        </li>
        <li>
          <svg viewBox="0 0 16 16" aria-hidden="true"><circle cx="8" cy="8" r="7" fill="#2c4a73"/><g fill="none" stroke="#fff" stroke-width="0.9"><circle cx="8" cy="8" r="4.5"/><ellipse cx="8" cy="8" rx="2" ry="4.5"/><path d="M3.5 8h9"/></g></svg>
          www.VantrePhysio.ca
        </li>
      </ul>
    </div>

    <p class="slogan">Mobile Physiotherapy - Your Road To Recovery</p>
    <div class="divider"></div>

    <div class="services">
      <h2 class="services-title">Services Including</h2>
      <ul class="services-list">
        <li>Physiotherapy</li>
        <li>Direct Billing</li>
        <li>Ims</li>
        <li>Acupuncture</li>
      </ul>
    </div>

    <div class="bottom-band"></div>
  </section>

</body>
</html>
```